Brightwren Farming

We need a logo design for a new company based in Kelowna, BC. We grow market garden vegetables for sale at market and in a CSA program. We try to only use hand tools for all aspects of cultivating, seeding, weeding, harvesting and distributing. For this reason we consider ourselves very low impact on the environment.

We would like blues and green in the design with an earthy, natural feel

Target Market(s)

Environmentally aware, health conscience

Industry/Entity Type

Farming

Requirements
Must have
• Foot prints with section for contact details all on the one side
Should not have
• Dark, black colours or anything that looks unnatural

```html
<!DOCTYPE html>
<html lang="en">
<head>
<meta charset="utf-8">
<title>Brightwren Farming – Business Card</title>
<link rel="stylesheet" href="https://fonts.googleapis.com/css2?family=Source+Sans+3:wght@600&display=swap">
<style>
  :root {
    --page: #f2f2f2;
    --card: #f4f1e6;
    --sky: #0f8fbf;
    --leaf: #5e9a3a;
    --soil: #3d5a2c;
    --sky-soft: #4fb8de;
  }
  html, body {
    margin: 0;
    width: 1200px;
    height: 1104px;
    overflow: hidden;
    background: var(--page);
    font-family: "Source Sans 3", "Helvetica Neue", Arial, sans-serif;
    font-weight: 600;
  }
  .business-card {
    position: absolute;
    left: 100px;
    top: 262px;
    width: 1000px;
    height: 580px;
    background: var(--card);
    overflow: hidden;
    box-shadow: 0 6px 24px rgba(0,0,0,0.18);
  }
  .card-swooshes {
    position: absolute;
    inset: 0;
    width: 1000px;
    height: 580px;
  }
  .brand {
    position: absolute;
    right: 530px;
    top: 226px;
    display: flex;
    align-items: center;
    gap: 14px;
  }
  .brand-dot {
    width: 26px;
    height: 26px;
    border-radius: 50%;
    background: var(--leaf);
    flex: none;
  }
  .brand-name {
    text-align: right;
    color: var(--sky);
    line-height: 1;
  }
  .brand-name .brand-main {
    display: block;
    font-size: 54px;
    letter-spacing: 1px;
  }
  .brand-name .brand-sub {
    display: block;
    font-size: 38px;
    margin-top: 6px;
  }
  .divider {
    position: absolute;
    left: 489px;
    top: 168px;
    width: 2px;
    height: 342px;
    background: var(--leaf);
  }
  .person {
    position: absolute;
    left: 504px;
    top: 164px;
  }
  .person-name {
    margin: 0;
    font-size: 38px;
    line-height: 1;
    font-weight: 600;
    color: var(--sky);
  }
  .person-title {
    margin: 4px 0 0;
    font-size: 18px;
    line-height: 1;
    color: var(--leaf);
  }
  .contact-list {
    position: absolute;
    left: 504px;
    top: 296px;
    margin: 0;
    padding: 0;
    list-style: none;
    color: var(--soil);
    font-size: 27px;
    line-height: 36px;
  }
  .contact-list li {
    display: flex;
    align-items: center;
  }
  .contact-icon {
    width: 18px;
    height: 18px;
    margin-right: 20px;
    fill: var(--sky);
    flex: none;
  }
</style>
</head>
<body>
  <section class="business-card">
    <svg class="card-swooshes" viewBox="0 0 1000 580" aria-hidden="true">
      <path d="M330 0 Q860 20 1000 250 L1000 0 Z" fill="var(--leaf)"/>
      <path d="M405 0 Q880 12 1000 181 L1000 0 Z" fill="var(--sky-soft)"/>
      <path d="M0 350 Q140 545 720 580 L0 580 Z" fill="var(--leaf)"/>
      <path d="M0 410 Q200 560 640 580 L0 580 Z" fill="var(--sky-soft)"/>
    </svg>

    <div class="brand">
      <span class="brand-dot"></span>
      <div class="brand-name">
        <span class="brand-main">BRIGHTWREN</span>
        <span class="brand-sub">Farming</span>
      </div>
    </div>

    <div class="divider"></div>

    <div class="person">
      <h1 class="person-name">MR. TOMAS REED</h1>
      <p class="person-title">MANAGING DIRECTOR</p>
    </div>

    <ul class="contact-list">
      <li>
        <svg class="contact-icon" viewBox="0 0 24 24" aria-hidden="true"><path d="M6.6 10.8a15 15 0 0 0 6.6 6.6l2.2-2.2c.3-.3.7-.4 1-.2 1.1.4 2.3.6 3.6.6.6 0 1 .4 1 1V20c0 .6-.4 1-1 1A17 17 0 0 1 3 4c0-.6.4-1 1-1h3.5c.6 0 1 .4 1 1 0 1.3.2 2.5.6 3.6.1.3 0 .7-.2 1z"/></svg>
        555-014-2290
      </li>
      <li>
        <svg class="contact-icon" viewBox="0 0 24 24" aria-hidden="true"><path d="M2 5h20v14H2z M3.5 6.5 12 13l8.5-6.5" stroke="var(--card)" stroke-width="1.6"/></svg>
        hello@brightwrenfarming.com
      </li>
      <li>
        <svg class="contact-icon" viewBox="0 0 24 24" aria-hidden="true"><circle cx="12" cy="12" r="10"/><path d="M2 12h20M12 2c3 3 3 17 0 20M12 2c-3 3-3 17 0 20" stroke="var(--card)" stroke-width="1.4" fill="none"/></svg>
        www.brightwrenfarming.com
      </li>
      <li>
        <svg class="contact-icon" viewBox="0 0 24 24" aria-hidden="true"><path d="M12 3 2 12h3v9h5v-6h4v6h5v-9h3z"/></svg>
        12 alder lane, upper ridge
      </li>
    </ul>
  </section>
</body>
</html>
```